Horse related business entrepreneur needs a business card

I need a business card design for my horse related business. The enterprise is Copper Vale LLC and I have 3 businesses (headquartered at 2 locations): 1. property management where we rent horse stalls and apartments at a thoroughbred training center outside Ocala; 2. a medium sized transportation service in central Florida that sells horse bedding and removes used horse bedding from horse farms; and horse racing

```html
<!DOCTYPE html>
<html lang="en">
<head>
<meta charset="utf-8">
<title>Copper Vale LLC – Business Card</title>
<link rel="stylesheet" href="https://fonts.googleapis.com/css2?family=Archivo+Black&family=Open+Sans:wght@400;600;700;800&display=swap">
<style>
  :root {
    --bg: #2a2a2a;
    --orange: #e8623a;
    --orange-light: #ef7042;
    --orange-dark: #c9471f;
    --orange-mid: #d9552b;
    --ink: #0c0c0c;
    --white: #ffffff;
    --grey: #8d8d8d;
    --photo-dark: #2f2f31;
    --photo-light: #6a6a6c;
  }
  * { margin: 0; padding: 0; box-sizing: border-box; }
  html, body { width: 1200px; height: 900px; overflow: hidden; }
  body {
    background: var(--bg);
    font-family: "Open Sans", Arial, sans-serif;
    position: relative;
  }
  .card {
    position: absolute;
    left: 320px;
    width: 560px;
    height: 320px;
    border-radius: 22px;
    overflow: hidden;
    box-shadow: 0 14px 30px rgba(0,0,0,.45);
  }
  /* Front */
  .card-front {
    top: 110px;
    background: linear-gradient(160deg, var(--orange-light), var(--orange) 60%, #e45a30);
  }
  .brand {
    position: absolute;
    top: 112px;
    left: 0; right: 0;
    text-align: center;
    font-family: "Archivo Black", "Arial Black", sans-serif;
    color: var(--ink);
    font-size: 40px;
    letter-spacing: 1px;
    line-height: 1;
  }
  .brand .brand-suffix { font-size: 22px; vertical-align: 14px; margin-left: 4px; }
  .front-footer {
    position: absolute;
    left: 36px; right: 30px; bottom: 34px;
    display: flex;
    align-items: center;
    gap: 16px;
    color: var(--white);
    font-size: 15px;
    line-height: 1.15;
  }
  .location-dot {
    width: 30px; height: 30px; border-radius: 50%;
    background: var(--ink); flex: none;
  }
  .divider { width: 2px; height: 44px; background: #8a5a48; margin: 0 8px; }
  /* Back */
  .card-back { top: 470px; background: var(--orange); }
  .card-back svg { position: absolute; inset: 0; }
  .name-band {
    position: absolute;
    top: 66px; right: 22px;
    text-align: right;
    color: var(--white);
    line-height: 1;
  }
  .person-name { font-size: 26px; font-weight: 400; letter-spacing: .5px; }
  .person-name strong { font-weight: 800; }
  .person-role { color: var(--grey); font-size: 15px; font-weight: 700; letter-spacing: 1px; margin-top: 2px; }
  .contact-list {
    position: absolute;
    top: 126px; right: 14px;
    list-style: none;
    color: var(--white);
    font-size: 16px;
  }
  .contact-list li {
    display: flex; justify-content: flex-end; align-items: center;
    height: 32px;
    border-bottom: 1px solid rgba(90,30,10,.5);
  }
  .contact-list .value { padding-right: 10px; }
  .contact-list .key {
    width: 24px; text-align: center;
    border-left: 1px solid rgba(255,255,255,.8);
    height: 100%; line-height: 32px;
    font-weight: 600;
  }
</style>
</head>
<body>
  <section class="card card-front" aria-label="Card front">
    <h1 class="brand">COPPER VALE<span class="brand-suffix">LLC</span></h1>
    <div class="front-footer">
      <span class="location-dot"></span>
      <address class="address">1742 NW 96th Lane<br>Redfield, FL 32610</address>
      <span class="divider"></span>
      <address class="address">5180 Willow Ridge Road<br>Ashford, VA 22930</address>
    </div>
  </section>

  <section class="card card-back" aria-label="Card back">
    <svg width="560" height="320" viewBox="0 0 560 320">
      <defs>
        <linearGradient id="photoTone" x1="0" y1="0" x2="1" y2="1">
          <stop offset="0" stop-color="var(--photo-light)"/>
          <stop offset="1" stop-color="var(--photo-dark)"/>
        </linearGradient>
      </defs>
      <polygon class="fold fold-dark" points="240,0 300,0 350,320 290,320" fill="var(--orange-dark)"/>
      <polygon class="fold fold-mid" points="262,0 322,0 372,320 312,320" fill="var(--orange-mid)"/>
      <polygon class="fold fold-front" points="286,0 560,0 560,320 398,320" fill="var(--orange)"/>
      <polygon class="photo-area" points="0,0 240,0 290,320 0,320" fill="url(#photoTone)" role="img" aria-label="Photo of a dark horse galloping"/>
      <rect class="name-band" x="205" y="58" width="380" height="52" rx="26" fill="var(--ink)"/>
    </svg>
    <div class="name-band">
      <p class="person-name"><strong>DANE</strong> PORTER</p>
      <p class="person-role">OWNER</p>
    </div>
    <ul class="contact-list">
      <li><span class="value">(434) 555-0148</span><span class="key">P</span></li>
      <li><span class="value">(434) 555-0193</span><span class="key">F</span></li>
      <li><span class="value">dane@coppervale.com</span><span class="key">E</span></li>
    </ul>
  </section>
</body>
</html>
```